RepHarborly.com "RE-SKIN" project

We have an existing site that we've recently built that needs to be re-formatted, skinned and polished. Our current developer did an amazing job building the backend but it not an expert in design and formatting of HTML and Web design. We need to have site cleaned up with all new formatting, layout, design elements and visual effects. ALl the date and functionality of the site will remain the same.

We would like to see Home page mock ups that may include Photo's, Flash, etc. or any other design element the designer feels would convey, a corporate, business oriented, simple and clean feel. The way the site currently looks is very basic and we need to have a slick, visual pleasing and easy to navigate design to go with our new functionality. The home page design will then need to translate over into the remaining pages of the site.

This is business to business site and will act as recruitment tool for medical device organizations. We have created a nationwide database of the top medical distributor groups (independent sale reps and groups). We act a "dating site" for medical manufacturers to find the best reps to sell their products.

NOTES on DESIGN:

* THE FUNCTION AND DATA OF THE SITE WILL REMAIN THE SAME, THIS PROJECT WILL BE TAKING ALL EXISTING INFO AND RE-DESIGNING THE LAYOUT.

*Must keep same color scheme

*Home Page design will be main focus and then ALL other pages need to follow style and template of Home page

* The sign up process on the site is in desperate need of re-design and we would like to see BIG, Step by Step, windows that make it feel very simple for the user to fill out (Best example we can think of is the Wellpathory.org site step by step sign up process. As bad as the overall functionality is on that site, the sign up process and drop down menu steps are easy to fill out.)

*The site is currently in a very basic "utilitarian" style and has very little in way of design, text formatting, and overall appearance. We need to have the designer go through each page and JUSTIFY, RE-SIZE, RE-SCALE and dress up all the current information displayed.

* We need the display pages to be easier to read, have better flow and more visually pleasing. (EXAMPLE: ANy search results that are done on the site come back in very table driven, hard to read, small text with small logo. We would like to see more design elements with updated formats and hopefully larger icons and east to read and navigate text

* WE ARE OPEN TO ANY DESIGN IDEAS OR MOCK UPS.

* Logos, icons, animation etc need to remain the same.

*Home page can feature video or photos but the remainder of the site will remian data only.
Updates

We would suggest doing a Mock up of the HOME PAGE only to begin with. We can then evaluate and choose a design theme/concept to carry over into the remainder of the pages.

Target Market(s)

Independent Medical Sales Distributors (sales reps) and Medical device manufacturers.

Industry/Entity Type

Recruitment

Coding

Coded - Design and coding required

Number of Pages Required

5+ page

Font styles to use
Sans Serif

Colors
0492cd
0455a3
3176b5
cedeed
85cae6
fcfdfe

Requirements
Must have
• *Must be Mobile Friendly
• *Must use all the info, links, logos and icons currently on www.RepHarborly.com
• *All pages of the site must follow to layout and design of the Home Page that is created in this project
• *Every page needs to be updated
Nice to have
• Glossy, crisp home page, that incorporate "stock" photos or animation for a more promotional or brochure type of feel
• Easy to navigate, bigger text and buttons and icons.
Should not have
• Color scheme and logo should not change

```html
<!DOCTYPE html>
<html lang="en">
<head>
<meta charset="utf-8">
<title>RepHarborly.com – Independent Medical Sales Resource</title>
<link rel="stylesheet" href="https://fonts.googleapis.com/css2?family=Poppins:wght@400;500;600;700&family=Open+Sans:ital,wght@0,400;0,600;0,700;1,400&family=Roboto+Condensed:wght@700&display=swap">
<style>
:root{
  --blue:#0492cd;
  --blue-dark:#0455a3;
  --blue-mid:#3176b5;
  --blue-pale:#cedeed;
  --sky:#85cae6;
  --band:#76bfe3;
  --white:#fcfdfe;
  --navy:#112f66;
  --navy-deep:#0d2756;
  --green:#6db33f;
  --ink:#222831;
  --text:#4a4f57;
  --line:#dfe3e8;
}
*{box-sizing:border-box;margin:0;padding:0}
html,body{width:1200px;height:3303px;overflow:hidden}
body{position:relative;background:var(--white);font-family:"Open Sans",sans-serif;color:var(--text)}
.abs{position:absolute}

/* header */
.site-header{left:0;top:0;width:1200px;height:115px;background:#fff;z-index:3}
.brand{left:132px;top:34px;display:flex;align-items:center;gap:10px}
.brand-square{width:50px;height:50px;border-radius:10px;background:var(--blue-dark)}
.brand-name{font-family:"Poppins",sans-serif;font-weight:600;font-size:31px;color:var(--ink);letter-spacing:-.5px}
.btn-sm{height:32px;border-radius:4px;color:#fff;font-family:"Poppins",sans-serif;font-size:13px;font-weight:500;display:flex;align-items:center;justify-content:center;gap:6px;text-transform:uppercase}
.btn-signup{left:636px;top:22px;width:92px;background:var(--green)}
.btn-login{left:742px;top:22px;width:90px;background:var(--blue)}
.header-search{left:852px;top:22px;width:216px;height:32px;border:1px solid #c8ccd2;border-radius:16px;font-size:11px;color:#888;display:flex;align-items:center;padding:0 14px;justify-content:space-between}
.main-nav{left:532px;top:74px;display:flex;gap:27px;font-family:"Poppins",sans-serif;font-weight:500;font-size:16px;color:var(--ink)}

/* hero */
.hero{left:0;top:115px;width:1200px;height:597px;background:linear-gradient(100deg,#7f97ad 0%,#b9c8d4 30%,#8ea3b5 55%,#4f6a82 80%,#2f4458 100%)}
.hero-shade{left:0;top:115px;width:1200px;height:597px;background:rgba(10,25,45,.28)}
.hero-title{left:0;top:334px;width:1200px;text-align:center;color:#fff;font-family:"Poppins",sans-serif;font-weight:600;font-size:28px;line-height:43px;text-transform:uppercase}
.hero-sub{left:0;top:438px;width:1200px;text-align:center;color:#fff;font-size:19px}
.search-panel{left:208px;top:515px;width:786px;height:66px;background:rgba(255,255,255,.35);border:1px solid rgba(255,255,255,.8);display:flex;gap:10px;padding:13px 14px}
.select{width:208px;height:40px;background:#fff;font-size:12px;color:#555;display:flex;align-items:center;justify-content:space-between;padding:0 14px}
.btn-search{width:104px;height:40px;background:var(--green);color:#fff;font-family:"Poppins",sans-serif;font-size:13px;display:flex;align-items:center;justify-content:center;gap:6px;border-radius:3px}
.hero-dots{left:560px;top:626px;display:flex;gap:10px;align-items:center}
.hero-dots span{width:12px;height:12px;border-radius:50%;background:#fff}
.hero-dots span.on{width:18px;height:18px;background:transparent;border:2px solid #fff;position:relative}
.hero-dots span.on::after{content:"";position:absolute;left:3px;top:3px;width:8px;height:8px;border-radius:50%;background:#fff}

/* choice band */
.choice-band{left:0;top:712px;width:1200px;height:433px;background:var(--band)}
.choice-card{top:784px;width:458px;height:280px;background:#fff;border-radius:0 0 40px 0;overflow:hidden}
.card-distributors{left:128px}
.card-lines{left:632px;border-radius:40px 0 0 0}
.card-photo{top:0;height:280px;width:190px}
.card-distributors .card-photo{left:0;background:linear-gradient(90deg,#dfe8f1,#f4f7fa)}
.card-lines .card-photo{right:0;background:linear-gradient(270deg,#b7cfe2,#eef3f8)}
.card-mark{width:50px;height:50px;border-radius:8px}
.card-title{font-family:"Roboto Condensed",sans-serif;font-weight:700;font-size:22px;color:var(--ink);text-transform:uppercase}
.card-text{font-size:13.5px;line-height:24px;color:#444;width:250px}
.btn-card{width:124px;height:36px;color:#fff;font-family:"Poppins",sans-serif;font-size:13px;font-weight:500;display:flex;align-items:center;justify-content:center;border-radius:3px;text-transform:uppercase}

/* featured */
.section-title{left:0;width:1200px;text-align:center;font-family:"Poppins",sans-serif;font-weight:500;color:var(--ink)}
.section-title em{font-style:normal;color:var(--blue-dark)}
.featured-title{top:1230px;font-size:38px}
.lines-table{left:132px;top:1335px;width:960px;border-collapse:collapse;background:#fff;box-shadow:0 2px 10px rgba(0,0,0,.15);table-layout:fixed}
.lines-table th{height:48px;background:#f1f2f4;font-family:"Poppins",sans-serif;font-weight:400;font-size:14px;color:#333;border:1px solid var(--line)}
.lines-table td{height:112px;vertical-align:top;padding:22px 14px 0 16px;font-size:11.5px;line-height:15px;color:#444;border:1px solid var(--line)}
.lines-table td.c{text-align:center;padding-left:0;padding-right:0}

/* search band */
.search-band{left:0;top:1865px;width:1200px;height:423px;background:linear-gradient(110deg,#3b3f45 0%,#23272d 45%,#34383e 100%)}
.search-band-title{top:1993px;font-size:40px;color:#fff;font-weight:600;text-transform:uppercase}
.search-band-sub{left:0;top:2062px;width:1200px;text-align:center;color:#fff;font-size:16px}
.btn-pill{left:527px;top:2120px;width:148px;height:38px;border-radius:19px;background:var(--blue-dark);color:#fff;font-family:"Poppins",sans-serif;font-weight:600;font-size:15px;display:flex;align-items:center;justify-content:center;text-transform:uppercase}

/* reviews */
.reviews{left:0;top:2288px;width:1200px;height:560px;background:linear-gradient(90deg,#e9eef3,#f6f8fa 40%,#e4eaf0)}
.reviews-title{top:2378px;font-size:32px;font-weight:600;text-transform:uppercase}
.review{top:2490px;width:385px}
.review-quote{font-size:13px;line-height:23px;font-style:italic;color:#555}
.review-quote::before{content:"\201C";font-size:22px;color:#999;margin-right:3px}
.reviewer{display:flex;align-items:center;gap:16px;margin-top:24px}
.avatar{width:70px;height:70px;border-radius:50%;background:linear-gradient(#c9b8a8,#8e7a6b);border:3px solid #fff}
.reviewer-name{font-family:"Poppins",sans-serif;font-size:12px;font-weight:500;color:var(--blue-mid);text-transform:uppercase;line-height:20px}
.review-divider{left:672px;top:2490px;width:1px;height:170px;background:#c9d0d8}

/* footer */
.footer-shapes{left:0;top:2730px;width:1200px;height:160px}
.site-footer{left:0;top:2850px;width:1200px;height:453px;background:var(--navy)}
.footer-heading{font-family:"Poppins",sans-serif;font-weight:600;font-size:19px;color:#fff;text-transform:uppercase}
.contact-item{display:flex;gap:14px;font-size:12px;line-height:18px;color:#fff;margin-top:20px}
.footer-text{font-size:11px;line-height:18px;color:#fff;width:310px}
.subscribe{left:392px;top:3017px;width:310px;height:36px;background:#fff;border-radius:18px;display:flex;align-items:center;justify-content:space-between;overflow:hidden}
.subscribe span{font-size:11px;color:#555;padding-left:16px}
.subscribe b{height:36px;width:102px;background:var(--blue);color:#fff;border-radius:18px;font-family:"Poppins",sans-serif;font-weight:600;font-size:12px;display:flex;align-items:center;justify-content:center;text-transform:uppercase}
.quick-links{list-style:none;font-size:11.5px;line-height:22px;color:#fff}
.footer-brand{left:973px;top:2955px;width:94px;height:94px;background:#fff;border-radius:16px;display:flex;align-items:center;justify-content:center;font-family:"Poppins",sans-serif;font-weight:600;font-size:12px;color:var(--navy)}
.footer-rule{left:0;top:3143px;width:1200px;height:1px;background:rgba(255,255,255,.25)}
.social{left:540px;top:3182px;display:flex;gap:8px}
.social span{width:26px;height:26px;border-radius:50%;border:1.5px solid #fff}
.copyright{left:0;top:3240px;width:1200px;text-align:center;font-size:12.5px;color:#fff}
</style>
</head>
<body>

<header class="site-header abs">
  <div class="brand abs"><span class="brand-square"></span><span class="brand-name">RepHarborly.com</span></div>
  <div class="btn-sm btn-signup abs">
    <svg width="11" height="11" viewBox="0 0 12 12"><circle cx="6" cy="3.5" r="3" fill="#fff"/><path d="M0 12c0-4 3-5.5 6-5.5s6 1.5 6 5.5z" fill="#fff"/></svg>Signup</div>
  <div class="btn-sm btn-login abs">
    <svg width="10" height="11" viewBox="0 0 10 12"><rect x="0" y="5" width="10" height="7" rx="1" fill="#fff"/><path d="M2.5 5V3.5a2.5 2.5 0 0 1 5 0V5" stroke="#fff" stroke-width="1.6" fill="none"/></svg>Log In</div>
  <div class="header-search abs">Search here
    <svg width="14" height="14" viewBox="0 0 14 14"><circle cx="6" cy="6" r="4.5" stroke="#555" stroke-width="1.5" fill="none"/><path d="M9.5 9.5L13 13" stroke="#555" stroke-width="1.5"/></svg></div>
  <nav class="main-nav abs"><span>HOME</span><span>HOW IT WORKS</span><span>PRODUCTS</span><span>RESOURCES</span><span>CONTACT US</span></nav>
</header>

<section>
  <div class="hero abs" role="img" aria-label="Photo of a businesswoman shaking hands with a doctor in a bright clinic"></div>
  <div class="hero-shade abs"></div>
  <h1 class="hero-title abs">The web's fastest growing<br>resource for independent medical sales</h1>
  <p class="hero-sub abs">We Match Distributors With Top Prospect Lines!</p>
  <div class="search-panel abs">
    <div class="select">Search For <svg width="8" height="5"><path d="M0 0h8L4 5z" fill="#444"/></svg></div>
    <div class="select">Select states <svg width="8" height="5"><path d="M0 0h8L4 5z" fill="#444"/></svg></div>
    <div class="select">Select Categories <svg width="8" height="5"><path d="M0 0h8L4 5z" fill="#444"/></svg></div>
    <div class="btn-search">SEARCH <svg width="12" height="12" viewBox="0 0 14 14"><circle cx="6" cy="6" r="4.5" stroke="#fff" stroke-width="2" fill="none"/><path d="M9.5 9.5L13 13" stroke="#fff" stroke-width="2"/></svg></div>
  </div>
  <div class="hero-dots abs"><span class="on"></span><span></span><span></span><span></span></div>
</section>

<section>
  <div class="choice-band abs"></div>
  <article class="choice-card card-distributors abs">
    <div class="card-photo abs" role="img" aria-label="Photo of a doctor writing on a clipboard"></div>
    <div class="card-mark abs" style="left:205px;top:30px;background:var(--green)"></div>
    <h2 class="card-title abs" style="left:205px;top:98px">I need distributors</h2>
    <p class="card-text abs" style="left:205px;top:140px">Find top medical distributor reps or groups to sell your product</p>
    <div class="btn-card abs" style="left:205px;top:212px;background:var(--green)">Sign up now</div>
  </article>
  <article class="choice-card card-lines abs">
    <div class="card-photo abs" role="img" aria-label="Photo of a smiling female doctor with a stethoscope"></div>
    <div class="card-mark abs" style="left:38px;top:30px;background:var(--blue-dark)"></div>
    <h2 class="card-title abs" style="left:38px;top:98px">I need new product lines</h2>
    <p class="card-text abs" style="left:38px;top:140px">Locate and secure the top available medical product lines in your area</p>
    <div class="btn-card abs" style="left:38px;top:212px;background:var(--blue-dark)">Sign up now</div>
  </article>
</section>

<section>
  <h2 class="section-title featured-title abs">Featured <em>Lines</em></h2>
  <table class="lines-table abs">
    <colgroup><col style="width:126px"><col style="width:116px"><col style="width:149px"><col style="width:159px"><col style="width:143px"><col style="width:138px"><col style="width:129px"></colgroup>
    <thead><tr><th>Title</th><th>Tracking ID</th><th>Location</th><th>Categories</th><th>Commission</th><th>Product Cost</th><th>Date Posted</th></tr></thead>
    <tbody>
      <tr><td>Another Product</td><td>1043-18</td><td>Purchase a product to view.</td><td>Capital Equipment<br>Diagnostic Imaging<br>Healthcare IT<br>Healthcare Software</td><td class="c">11%-20%</td><td class="c">$100-$500</td><td class="c">12/6/2017</td></tr>
      <tr><td>Another Product</td><td>1043-18</td><td>Purchase a product to view.</td><td>Capital Equipment<br>Diagnostic Imaging<br>Healthcare IT<br>Healthcare Software</td><td class="c">11%-20%</td><td class="c">$100-$500</td><td class="c">12/6/2017</td></tr>
      <tr><td>Another Product</td><td>1043-18</td><td>Purchase a product to view.</td><td>Capital Equipment<br>Diagnostic Imaging<br>Healthcare IT<br>Healthcare Software</td><td class="c">11%-20%</td><td class="c">$100-$500</td><td class="c">12/6/2017</td></tr>
    </tbody>
  </table>
</section>

<section>
  <div class="search-band abs" role="img" aria-label="Photo of a businessman with a phone and laptop on office stairs"></div>
  <h2 class="section-title search-band-title abs">Search for distributors</h2>
  <p class="search-band-sub abs">Locate and secure the top distributors in the medical industry!</p>
  <div class="btn-pill abs">Sign up now</div>
</section>

<section>
  <div class="reviews abs" role="img" aria-label="Faint photo of medical professionals in conversation"></div>
  <h2 class="section-title reviews-title abs">Customer <em>Reviews</em></h2>
  <div class="review abs" style="left:185px">
    <p class="review-quote">Lorem ipsum dolor sit amet, consectetur adipisicing elit, sed do eiusmod tempor incididunt ut labore et dolore magna aliqua Unde omnis, consequuntur.</p>
    <div class="reviewer"><div class="avatar" role="img" aria-label="Reviewer portrait"></div><div class="reviewer-name">Marla Tensing<br>Rep Harborly</div></div>
  </div>
  <div class="review-divider abs"></div>
  <div class="review abs" style="left:672px;padding-left:0">
    <p class="review-quote">Lorem ipsum dolor sit amet, consectetur adipisicing elit, sed do eiusmod tempor incididunt ut labore et dolore magna aliqua Unde omnis, consequuntur.</p>
    <div class="reviewer"><div class="avatar" role="img" aria-label="Reviewer portrait"></div><div class="reviewer-name">Devon Ashcroft<br>Rep Harborly</div></div>
  </div>
</section>

<footer>
  <svg class="footer-shapes abs" viewBox="0 0 1200 160" preserveAspectRatio="none">
    <polygon points="0,10 170,40 0,90" fill="var(--blue)"/>
    <polygon points="0,40 1200,110 1200,160 0,160" fill="var(--navy)"/>
    <polygon points="1020,100 1200,70 1200,146" fill="var(--blue)"/>
  </svg>
  <div class="site-footer abs"></div>

  <div class="abs" style="left:132px;top:2910px">
    <h3 class="footer-heading">Contact Us</h3>
    <div class="contact-item"><svg width="14" height="18" viewBox="0 0 14 18"><path d="M7 1a6 6 0 0 1 6 6c0 4.5-6 10-6 10S1 11.5 1 7a6 6 0 0 1 6-6z" stroke="#fff" stroke-width="1.3" fill="none"/><circle cx="7" cy="7" r="2" stroke="#fff" stroke-width="1.3" fill="none"/></svg><span>Rep Harborly<br>Keelson Lane, Bayford 4127<br>Northshire</span></div>
    <div class="contact-item"><svg width="14" height="14" viewBox="0 0 16 16"><path d="M3 1l3 3-2 2c1 2 3 4 5 5l2-2 3 3-2 3C6 15 1 10 0 3z" stroke="#fff" stroke-width="1.2" fill="none"/></svg><span>Phone : 1300 555 018</span></div>
    <div class="contact-item"><svg width="15" height="12" viewBox="0 0 16 12"><rect x=".7" y=".7" width="14.6" height="10.6" stroke="#fff" stroke-width="1.2" fill="none"/><path d="M1 1l7 6 7-6" stroke="#fff" stroke-width="1.2" fill="none"/></svg><span>info@repharborly.com</span></div>
  </div>

  <div class="abs" style="left:392px;top:2910px">
    <h3 class="footer-heading">Sign up to receive email</h3>
    <p class="footer-text" style="margin-top:18px">Excepteur sint occaecat cupidatat non proident, sunt in culpa qui Nemo enim ipsam voluptatem</p>
  </div>
  <div class="subscribe abs"><span>Enter Email</span><b>Subscribe</b></div>

  <div class="abs" style="left:795px;top:2910px">
    <h3 class="footer-heading">Quick Links</h3>
    <ul class="quick-links" style="margin-top:18px"><li>How it Works</li><li>Signup</li><li>Products</li><li>Resources</li><li>About Us</li><li>Contact Us</li><li>Terms &amp; Conditions</li></ul>
  </div>
  <div class="footer-brand abs">RepHarborly</div>

  <div class="footer-rule abs"></div>
  <div class="social abs"><span></span><span></span><span></span><span></span></div>
  <p class="copyright abs">Copyright © Rep Harborly 2018. All rights reserved.</p>
</footer>

</body>
</html>
```